Security Camera Sign

14” high x 11” wide Color: Blue, Yellow, Black and white

Make the sign vertical
Replace red with blue
WARNING: Black over yellow
These premises are protected by Closed Circuit Television: On white
Images are recorded for crime prevention and public safety. Unauthorized access, theft or vandalism will result in prosecution: On Blue

Target Market(s)

Outdoor commercial building

Industry/Entity Type

Security

Requirements
Nice to have
• I would like the sign stand out. If you need more colors? Thanks Ok

```html
<!DOCTYPE html>
<html lang="en">
<head>
<meta charset="utf-8">
<title>CCTV Warning Sign</title>
<link rel="stylesheet" href="https://fonts.googleapis.com/css2?family=Archivo+Black&family=Oswald:wght@600&display=swap">
<style>
  :root {
    --sign-blue: #1f3f95;
    --alert-yellow: #fff200;
    --ink-black: #161616;
    --panel-white: #ffffff;
    --camera-light: #9a9a9a;
    --camera-dark: #3a3a3a;
  }
  html, body {
    margin: 0;
    padding: 0;
    overflow: hidden;
    background: var(--sign-blue);
  }
  .sign {
    position: relative;
    width: 943px;
    height: 1200px;
    background: var(--sign-blue);
    overflow: hidden;
  }
  .headline-band {
    position: absolute;
    left: 33px;
    top: 38px;
    width: 875px;
    height: 134px;
    background: var(--alert-yellow);
  }
  .headline-band svg {
    display: block;
    width: 100%;
    height: 100%;
  }
  .headline-text {
    font-family: "Archivo Black", "Arial Black", sans-serif;
    font-size: 138px;
    fill: var(--ink-black);
  }
  .notice-panel {
    position: absolute;
    left: 33px;
    top: 207px;
    width: 875px;
    height: 594px;
    background: var(--panel-white);
  }
  .notice-statement {
    position: absolute;
    left: 22px;
    top: 16px;
    margin: 0;
    font-family: "Oswald", "Arial Narrow", sans-serif;
    font-weight: 600;
    font-size: 66px;
    line-height: 81px;
    letter-spacing: -2px;
    text-transform: uppercase;
    color: var(--ink-black);
  }
  .notice-statement span {
    display: block;
    white-space: nowrap;
  }
  .camera-illustration {
    position: absolute;
    left: 350px;
    top: 14px;
    width: 515px;
    height: 566px;
    background: linear-gradient(160deg, var(--camera-light) 0%, #6b6b6b 45%, var(--camera-dark) 100%);
    border-radius: 6px;
  }
  .legal-notice {
    position: absolute;
    left: 52px;
    top: 846px;
    margin: 0;
    font-family: "Archivo Black", "Arial Black", sans-serif;
    font-size: 45px;
    line-height: 65px;
    letter-spacing: 0.5px;
    text-transform: uppercase;
    color: var(--panel-white);
  }
  .legal-notice span {
    display: block;
    white-space: nowrap;
  }
</style>
</head>
<body>
  <main class="sign">
    <header class="headline-band">
      <svg viewBox="0 0 875 134" aria-label="Warning!!!">
        <text class="headline-text" x="20" y="117" textLength="835" lengthAdjust="spacingAndGlyphs">WARNING !!!</text>
      </svg>
    </header>

    <section class="notice-panel">
      <h1 class="notice-statement">
        <span>These</span>
        <span>Premises</span>
        <span>Are</span>
        <span>Protected</span>
        <span>By Closed</span>
        <span>Circuit</span>
        <span>Television</span>
      </h1>
      <div class="camera-illustration" role="img" aria-label="Illustration of a grey wall-mounted security camera with hood and bracket"></div>
    </section>

    <p class="legal-notice">
      <span>Images are recorded for</span>
      <span>crime prevention and public</span>
      <span>safety. Unauthorized</span>
      <span>access, theft or vandalism</span>
      <span>will result in prosecution</span>
    </p>
  </main>
</body>
</html>
```